Sign Advertisment for Condominium Development

I need a sign created that will be placed in front of a building that is being converted into a luxury condominium development.

The sign needs to say:

Two, Boutique Luxury Condominiums Delivering late 2015.

Luxury Finishes // Designer Kitchens and Bath // Each Unit over 2,000 Square Feet

Deeded Parking Included with Each Unit

To Learn More, Contact:

Marissa Talbot or Vernon Pike
(202) 555-0147
Marissa.Talbot@example-realty.com

I need a small disclaimer at the bottom stating:

These Condominium(s) have not been registered by the Office of Residential Standards and Property Oversight Bureau Tenancy Transition and Transfer Section. A Condominium Unit may be reserved on a non-binding reservation agreement, but no contract of sale or lease that is binding on the purchaser may be entered into prior to registration.

Target Market(s)

Young professionals seeking luxury condominium

Industry/Entity Type

Building

Font styles to use
Serif

Colors
00a88f
ffffff

```html
<!DOCTYPE html>
<html lang="en">
<head>
<meta charset="utf-8">
<title>Boutique Luxury Condominiums Sign</title>
<link href="https://fonts.googleapis.com/css2?family=Marcellus+SC&family=Questrial&display=swap" rel="stylesheet">
<style>
  :root {
    --page-bg: #eef3f7;
    --ink: #000000;
    --paper: #ffffff;
    --brand-teal: #00a88f;
    --text-dark: #1a1a1a;
    --fine-print: #555555;
    --skyline-top: #e4e4e4;
    --skyline-mid: #cfcfcf;
  }
  html, body {
    margin: 0;
    width: 1200px;
    height: 1000px;
    overflow: hidden;
    background: var(--page-bg);
  }
  .sign {
    position: absolute;
    left: 97px;
    top: 183px;
    width: 1005px;
    height: 647px;
    background: var(--paper);
    border: 1px solid var(--ink);
    box-sizing: border-box;
    font-family: "Questrial", "Century Gothic", sans-serif;
  }
  .headline-band {
    position: absolute;
    left: 0; top: 0;
    width: 100%;
    height: 257px;
    background: var(--ink);
    color: var(--paper);
    font-family: "Marcellus SC", "Trajan Pro", serif;
  }
  .headline-line {
    position: absolute;
    margin: 0;
    font-weight: 400;
    white-space: nowrap;
    line-height: 1;
  }
  .headline-count { left: 25px; top: 12px; font-size: 92px; letter-spacing: 7.5px; }
  .headline-type { left: 25px; top: 94px; font-size: 112px; letter-spacing: 10px; }
  .headline-delivery { right: 62px; top: 198px; font-size: 46px; letter-spacing: 3px; }

  .skyline {
    position: absolute;
    left: 488px; top: 265px;
    width: 440px;
    height: 292px;
    background: linear-gradient(180deg, var(--skyline-top) 0%, var(--skyline-mid) 50%, var(--paper) 100%);
    opacity: 0.55;
  }
  .features {
    position: absolute;
    left: 25px; top: 269px;
    margin: 0;
    font-size: 26px;
    line-height: 34px;
    letter-spacing: 0.2px;
    color: var(--text-dark);
    white-space: nowrap;
    z-index: 2;
  }
  .features .separator { color: var(--brand-teal); }

  .contact-box {
    position: absolute;
    left: 0; top: 372px;
    width: 406px;
    height: 175px;
    background: var(--ink);
    color: var(--paper);
    box-sizing: border-box;
    padding: 10px 0 0 27px;
    white-space: nowrap;
  }
  .contact-box p { margin: 0; }
  .contact-lead { font-size: 17px; line-height: 22px; }
  .contact-names { font-size: 25px; line-height: 34px; }
  .contact-phone { font-size: 47px; line-height: 52px; }
  .contact-email { font-size: 21px; line-height: 30px; }

  .disclaimer {
    position: absolute;
    left: 27px; top: 570px;
    width: 920px;
    margin: 0;
    font-size: 13px;
    line-height: 17px;
    color: var(--fine-print);
  }
</style>
</head>
<body>
  <main class="sign">
    <header class="headline-band">
      <h1 class="headline-line headline-count">2 Boutique Luxury</h1>
      <p class="headline-line headline-type">Condominiums</p>
      <p class="headline-line headline-delivery">Delivering late 2015</p>
    </header>

    <div class="skyline" role="img" aria-label="Faint grey city skyline illustration"></div>

    <p class="features">Luxury Finishes <span class="separator">&#8226;</span> Designer Kitchens &amp; Bath<br>Each Unit over 2,000 Square Feet &nbsp;<span class="separator">&#8226;</span> Deeded Parking Included with Each Unit</p>

    <section class="contact-box">
      <p class="contact-lead">To Learn More, Contact:</p>
      <p class="contact-names">Marissa Talbot or Vernon Pike</p>
      <p class="contact-phone">(202) 555-0147</p>
      <p class="contact-email">Marissa.Talbot@example-realty.com</p>
    </section>

    <p class="disclaimer">These Condominium(s) have not been registered by the Office of Residential Standards and Property Oversight Bureau Tenancy Transition and Transfer Section. A Condominium Unit may be reserved on a non-binding reservation agreement, but no contract of sale or lease that is binding on the purchaser may be entered into prior to registration.</p>
  </main>
</body>
</html>
```